Business Card Design Project

Hello Designers, hope you are all aiming enjoy the weekend
I have the Business Logo (uploaded), you can alter the color which ever way you think would work,
Im looking for a simple yet striking feel, something which will stay memorable (I have uploaded 3 examples for you to flick through)
Information on the card, will just be the bare minimum,
Double Sided
Info being
i.e.
Name
Number
Website
ABN
Tobin Wexmoor
+468213579 (singapore)
+315792846 (Australia)
+729384615 (America)
www.lomevu-linkup.example
ABN 86420913
Enjoy,
Tobin
Industry/Entity Type
Business
Look and feel
Each slider illustrates characteristics of the customer's brand and the style your logo design should communicate.

```html
<!DOCTYPE html>
<html lang="en">
<head>
<meta charset="utf-8">
<title>Lomevu Linkup — Business Card</title>
<link rel="stylesheet" href="https://fonts.googleapis.com/css2?family=Open+Sans:wght@400;700&display=swap">
<style>
  :root {
    --stage: #e9eaec;
    --card: #ffffff;
    --sky: #6cc3f0;
    --sky-deep: #3aa6e6;
    --name-blue: #4aa9e4;
    --ink: #2a2a2a;
    --brand: #c8203f;
    --card-w: 600px;
    --card-h: 343px;
  }
  * { box-sizing: border-box; margin: 0; padding: 0; }
  html, body {
    width: 1200px; height: 944px; overflow: hidden;
    background: var(--stage);
    font-family: "Open Sans", Arial, sans-serif;
  }
  .canvas { position: relative; width: 1200px; height: 944px; }
  .card {
    position: absolute;
    width: var(--card-w); height: var(--card-h);
    background: var(--card);
    box-shadow: 0 10px 24px rgba(0,0,0,.18);
    overflow: hidden;
  }
  .card--front { left: 70px; top: 80px; }
  .card--back { left: 530px; top: 510px; }
  .card__shapes { position: absolute; inset: 0; width: 100%; height: 100%; }
  .name-badge {
    position: absolute; top: -30px;
    width: 170px; height: 170px; border-radius: 50%;
    background: var(--card);
    display: flex; flex-direction: column; align-items: center; justify-content: center;
    padding-top: 24px;
    color: var(--name-blue); font-weight: 700; font-size: 20px;
    line-height: 1.15; letter-spacing: 1px; text-transform: uppercase; text-align: center;
  }
  .card--front .name-badge { left: 160px; }
  .card--back .name-badge { left: 215px; }
  .brand {
    position: absolute; left: 40px; top: 160px;
    display: flex; align-items: center; gap: 16px;
    color: var(--brand); font-weight: 700; font-size: 46px; letter-spacing: .5px;
  }
  .brand__mark { width: 44px; height: 44px; background: var(--brand); border-radius: 6px; }
  .contact {
    position: absolute; left: 175px; top: 150px;
    list-style: none; color: var(--ink);
    font-size: 18px; line-height: 1.45;
  }
</style>
</head>
<body>
<main class="canvas">
  <section class="card card--front" aria-label="Card front">
    <svg class="card__shapes" viewBox="0 0 600 343" preserveAspectRatio="none" aria-hidden="true">
      <defs>
        <linearGradient id="front-sky" x1="0" y1="0" x2="1" y2="1">
          <stop offset="0" stop-color="#3aa6e6"/>
          <stop offset="1" stop-color="#7ccdf3"/>
        </linearGradient>
      </defs>
      <polygon points="0,0 470,0 530,30 280,343 0,343" fill="url(#front-sky)"/>
    </svg>
    <div class="name-badge"><span>Tobin</span><span>Wexmoor</span></div>
    <div class="brand"><span class="brand__mark"></span><span class="brand__name">Lomevu Linkup</span></div>
  </section>

  <section class="card card--back" aria-label="Card back">
    <svg class="card__shapes" viewBox="0 0 600 343" preserveAspectRatio="none" aria-hidden="true">
      <defs>
        <linearGradient id="back-sky" x1="0" y1="0" x2="1" y2="1">
          <stop offset="0" stop-color="#7ccdf3"/>
          <stop offset="1" stop-color="#5bbbee"/>
        </linearGradient>
      </defs>
      <polygon points="40,0 470,0 560,80 250,343 0,343 0,40" fill="url(#back-sky)"/>
    </svg>
    <div class="name-badge"><span>Tobin</span><span>Wexmoor</span></div>
    <ul class="contact">
      <li>+468213579 (singapore)</li>
      <li>+315792846 (Australia)</li>
      <li>+729384615 (America)</li>
      <li>www.lomevu-linkup.example</li>
      <li>ABN 86420913</li>
    </ul>
  </section>
</main>
</body>
</html>
```